Business Card for Yachting Management Company

Need a business card design for a new yachting project management company. Attached is the logo for the company.
Our clients are large yacht owners and captains.
Design must be in the style of the logo. Modern, elegant.

Example of data to show:
Peter Hollis
Project Manager
(+38) 612 738 104
peter@quorvane.net
Quorvane Management - Meridel Tower, Office 22 - KRB - Port Vellmar

The data above will have to be changed (by me) for the different people in the company over the next years.

Will be printed using PrintNova (Lustre Card Series). They provide these guidelines for the size:
"the actual size of the card is 1050 x 600 pixels. However, the full bleed size is 1083 x 633 pixels, and the safe printing area is 1008 x 558 pixels."

```html
<!DOCTYPE html>
<html lang="en">
<head>
<meta charset="utf-8">
<title>Quorvane Management – Business Card</title>
<link rel="stylesheet" href="https://fonts.googleapis.com/css2?family=Exo+2:wght@700&family=Roboto:wght@400;500&display=swap">
<style>
  :root {
    --backdrop: #b08a68;
    --card-dark: #030303;
    --card-slate: #1b2126;
    --brand-blue: #1a76c9;
    --text-grey: #8d9296;
    --mark-grey: #7f8285;
  }
  * { box-sizing: border-box; margin: 0; padding: 0; }
  html, body { width: 1200px; height: 1122px; overflow: hidden; }
  body {
    background: var(--backdrop);
    font-family: "Roboto", Arial, sans-serif;
    position: relative;
  }
  .card {
    position: absolute;
    left: 170px;
    width: 860px;
    height: 491px;
    border-radius: 28px;
    background: linear-gradient(115deg, var(--card-dark) 0%, var(--card-dark) 40%, var(--card-slate) 100%);
    box-shadow: 0 10px 24px rgba(0,0,0,0.35);
    overflow: hidden;
  }
  .card--front { top: 48px; }
  .card--back { top: 583px; }

  .brand {
    position: absolute;
    display: flex;
    align-items: center;
    gap: 14px;
    color: var(--brand-blue);
    font-family: "Roboto", Arial, sans-serif;
    font-weight: 500;
    text-transform: uppercase;
    letter-spacing: 0.14em;
    white-space: nowrap;
  }
  .brand__square {
    width: 34px;
    height: 34px;
    background: var(--mark-grey);
    flex: none;
  }
  .card--front .brand {
    left: 50%;
    top: 50%;
    transform: translate(-50%, -50%);
    font-size: 36px;
  }
  .card--back .brand {
    right: 70px;
    top: 150px;
    font-size: 26px;
  }
  .card--back .brand__square { width: 26px; height: 26px; }

  .person { position: absolute; left: 70px; top: 196px; }
  .person__name {
    font-family: "Exo 2", Arial, sans-serif;
    font-weight: 700;
    font-size: 31px;
    letter-spacing: 0.02em;
    text-transform: uppercase;
    color: var(--brand-blue);
    line-height: 1;
  }
  .person__role {
    margin-top: 6px;
    font-size: 17px;
    color: var(--text-grey);
  }
  .divider {
    position: absolute;
    left: 60px;
    right: 60px;
    top: 282px;
    height: 2px;
    background: var(--brand-blue);
  }
  .contacts {
    position: absolute;
    left: 70px;
    top: 298px;
    list-style: none;
    font-size: 17px;
    color: var(--text-grey);
    letter-spacing: 0.03em;
  }
  .contacts li {
    display: flex;
    align-items: center;
    gap: 10px;
    line-height: 28px;
  }
  .contacts svg { width: 14px; height: 14px; fill: var(--brand-blue); flex: none; }
  .address {
    position: absolute;
    right: 70px;
    top: 300px;
    text-align: right;
    font-size: 17px;
    line-height: 26px;
    color: var(--text-grey);
    letter-spacing: 0.02em;
  }
</style>
</head>
<body>

  <section class="card card--front" aria-label="Card front">
    <div class="brand"><span class="brand__square"></span>Quorvane Management</div>
  </section>

  <section class="card card--back" aria-label="Card back">
    <div class="brand"><span class="brand__square"></span>Quorvane Management</div>

    <div class="person">
      <p class="person__name">Peter Hollis</p>
      <p class="person__role">Project Manager</p>
    </div>

    <div class="divider"></div>

    <ul class="contacts">
      <li>
        <svg viewBox="0 0 24 24" aria-hidden="true"><path d="M6.6 10.8a15.1 15.1 0 0 0 6.6 6.6l2.2-2.2a1 1 0 0 1 1-.25 11.4 11.4 0 0 0 3.6.57 1 1 0 0 1 1 1V20a1 1 0 0 1-1 1A17 17 0 0 1 3 4a1 1 0 0 1 1-1h3.5a1 1 0 0 1 1 1c0 1.25.2 2.45.57 3.57a1 1 0 0 1-.25 1z"/></svg>
        (+38) 612 738 104
      </li>
      <li>
        <svg viewBox="0 0 24 24" aria-hidden="true"><path d="M2 5h20v14H2zM3.5 6.5 12 13l8.5-6.5z" fill-rule="evenodd"/></svg>
        peter@quorvane.net
      </li>
    </ul>

    <p class="address">Quorvane Management-Meridel Tower<br>Office 22 - KRB-Port Vellmar</p>
  </section>

</body>
</html>
```